VELKORIS Stationery Design Project

I want a stationery design for a web development company consists of:
1- business card
2- Letter Head
3- small Envelope
4- Large Envelope

need a very clean professional simple design yet creative,

The company logo is attached
http://www.pixelbazaarhub.net/project-progress/designs.aspx?briefId=5830174&submissionId=47210938

logo font is sui generis rg (attached)
I would like to have the stationery text font to be helvetica font regular or light (can be changed)

I love the combination of cyan, black and grey colors
( will attach some recommended styles)

Business

• curves or waves

```html
<!DOCTYPE html>
<html lang="en">
<head>
<meta charset="utf-8">
<title>VELKORIS Business Card</title>
<link href="https://fonts.googleapis.com/css2?family=Arimo:wght@400&display=swap" rel="stylesheet">
<style>
  :root {
    --ink: #2a2a2a;
    --paper: #f4f4f4;
    --cyan: #1e9ad6;
    --grey: #8e8e8e;
    --text: #2b2b2b;
    --rule: #c8c8c8;
    --stage: #e2e3e5;
  }
  * { margin: 0; padding: 0; box-sizing: border-box; }
  html, body { width: 1200px; height: 900px; overflow: hidden; }
  body {
    background: var(--stage);
    font-family: "Arimo", Helvetica, Arial, sans-serif;
    display: flex;
    flex-direction: column;
    align-items: center;
    justify-content: center;
    gap: 60px;
  }
  .card {
    position: relative;
    width: 560px;
    height: 320px;
    box-shadow: 0 6px 18px rgba(0,0,0,0.18);
    overflow: hidden;
  }
  /* Front */
  .card-front { background: var(--ink); }
  .card-front .accent-bar {
    position: absolute;
    top: 0;
    right: 0;
    width: 250px;
    height: 26px;
    background: var(--cyan);
  }
  .card-front .edge-tick {
    position: absolute;
    left: 0;
    bottom: 44px;
    width: 4px;
    height: 34px;
    background: var(--cyan);
    box-shadow: 8px 0 0 var(--cyan);
  }
  .brand {
    position: absolute;
    left: 44px;
    bottom: 44px;
    display: flex;
    align-items: center;
    gap: 14px;
  }
  .brand-square {
    width: 30px;
    height: 30px;
    background: var(--grey);
  }
  .brand-name {
    font-size: 30px;
    letter-spacing: 2px;
    color: var(--cyan);
    line-height: 1;
  }
  /* Back */
  .card-back {
    background: var(--paper);
    color: var(--text);
    display: flex;
    align-items: center;
    padding-left: 72px;
  }
  .person { width: 170px; }
  .person-name { font-size: 21px; line-height: 1.15; }
  .person-title { font-size: 13px; margin-top: 3px; }
  .divider {
    width: 1px;
    height: 120px;
    background: var(--rule);
    margin: 0 22px 0 10px;
  }
  .contact { font-size: 13.5px; line-height: 1.3; }
  .contact-group + .contact-group { margin-top: 14px; }
  .contact-group p { margin: 0; }
</style>
</head>
<body>
  <section class="card card-front" aria-label="Business card front">
    <div class="accent-bar"></div>
    <div class="edge-tick"></div>
    <div class="brand">
      <div class="brand-square"></div>
      <span class="brand-name">VELKORIS</span>
    </div>
  </section>

  <section class="card card-back" aria-label="Business card back">
    <div class="person">
      <p class="person-name">Daniel Reyes</p>
      <p class="person-title">Vice President</p>
    </div>
    <div class="divider"></div>
    <div class="contact">
      <div class="contact-group">
        <p>415-902-318</p>
        <p>dreyes@velkoris.com</p>
        <p>www.velkoris.com</p>
      </div>
      <div class="contact-group">
        <p>18-40 Linden Avenue</p>
        <p>Oakridge, NJ 07438</p>
      </div>
    </div>
  </section>
</body>
</html>
```